Project Sign for Construction Company

Site contractor needs a 4'x8' sign to place on construction sites for advertising. Our company builds the infrastructure for new housing developments. These sign will be posted on the road side to be viewed by passing cars. I want a clean and bold look and feel that resembles my company logo.

Font styles to use
Other font styles liked:
• Hypatia Sans Pro

Colors

Designer to choose colors to be used in the design.

Requirements
Must have
• 555-318-2946 | Info@MarlowTerraworks.example
• CUC 8841907
• www.MarlowTerraworks.example
• Services
• Road Construction
• Site Preparation & Excavation
• Underground Utilities
• Shoreline Restoration
Nice to have
• Now Hiring
• Pipe Layers
• Foremen
• Equipment Operators
Should not have
• Should not have stock picture images used in the design, focus on logo and geometric shapes

```html
<!DOCTYPE html>
<html lang="en">
<head>
<meta charset="utf-8">
<title>Marlow Terraworks – Now Hiring Sign</title>
<link rel="stylesheet" href="https://fonts.googleapis.com/css2?family=Anton&family=Roboto+Condensed:wght@300;400&family=Roboto:wght@400;700&display=swap">
<style>
  :root {
    --brand-blue: #0a55a8;
    --brand-blue-deep: #084a93;
    --charcoal: #282828;
    --page-grey: #f0f0f0;
    --white: #ffffff;
    --ink: #3c3c3c;
    --rule-grey: #bdbdbd;
    --mark-tint: #dfe7f2;
  }
  * { box-sizing: border-box; margin: 0; padding: 0; }
  html, body {
    width: 1200px; height: 3000px; overflow: hidden;
    background: var(--page-grey);
  }
  .sign {
    position: absolute; left: 50px; top: 400px;
    width: 1100px; height: 2200px;
    background: var(--white);
    box-shadow: 0 30px 60px rgba(0,0,0,0.22);
    overflow: hidden;
  }
  .brand-mark {
    position: absolute; left: 278px; top: 160px;
    width: 545px; height: 496px;
    background: radial-gradient(ellipse at center, #c9d8ec 0%, var(--mark-tint) 60%, var(--white) 100%);
  }
  .brand-name {
    position: absolute; left: 0; right: 0; top: 690px;
    text-align: center;
    font-family: "Roboto", sans-serif; font-weight: 700;
    color: var(--brand-blue);
    line-height: 1;
  }
  .brand-name .line-one { display: block; font-size: 118px; letter-spacing: 6px; }
  .brand-name .line-two { display: block; font-size: 58px; letter-spacing: 9px; margin-top: 14px; }
  .services-band {
    position: absolute; left: 0; right: 0; top: 1099px; height: 437px;
    background: var(--charcoal);
    box-shadow: 0 -8px 14px rgba(0,0,0,0.12), 0 10px 14px rgba(0,0,0,0.18);
  }
  .hiring-banner {
    position: absolute; left: 102px; top: 981px;
    width: 897px; height: 228px;
    background: var(--brand-blue);
    display: flex; align-items: center; justify-content: center;
    font-family: "Anton", sans-serif; font-size: 176px; font-weight: 400;
    color: var(--white); letter-spacing: 1px; line-height: 1;
    box-shadow: 0 10px 18px rgba(0,0,0,0.3);
  }
  .service-list {
    position: absolute; left: 91px; top: 1310px;
    width: 960px;
    display: grid; grid-template-columns: 504px 1fr; row-gap: 52px;
    list-style: none;
    font-family: "Roboto Condensed", sans-serif; font-weight: 300;
    font-size: 38px; line-height: 48px; color: var(--white);
  }
  .service-list li { display: flex; align-items: center; gap: 14px; white-space: nowrap; }
  .service-list svg { width: 30px; height: 30px; flex: none; }
  .call-panel {
    position: absolute; left: 102px; top: 1538px;
    width: 884px; height: 375px;
    border: 10px solid #d4d4d4; border-top: none;
    border-radius: 0 0 52px 52px;
    background: var(--brand-blue);
    box-shadow: 0 26px 22px -14px rgba(0,0,0,0.35);
    display: flex; flex-direction: column; align-items: center; justify-content: center;
    font-family: "Anton", sans-serif; color: var(--white);
    font-size: 138px; line-height: 1.02; letter-spacing: 1px;
  }
  .contact-line {
    position: absolute; left: 0; right: 0; top: 1995px;
    text-align: center; white-space: nowrap;
    font-family: "Roboto", sans-serif; font-weight: 400;
    font-size: 29px; color: var(--ink);
  }
  .contact-line .divider { display: inline-block; margin: 0 10px; }
  .licence {
    position: absolute; left: 50%; top: 2070px;
    transform: translateX(-50%);
    padding: 4px 28px;
    border: 2px solid var(--ink);
    font-family: "Roboto", sans-serif; font-size: 36px; color: var(--ink);
    white-space: nowrap;
  }
</style>
</head>
<body>
  <main class="sign">
    <div class="brand-mark" role="img" aria-label="Company emblem artwork in blue line drawing"></div>
    <h1 class="brand-name">
      <span class="line-one">MARLOW</span>
      <span class="line-two">TERRAWORKS</span>
    </h1>

    <div class="services-band"></div>
    <h2 class="hiring-banner">NOW HIRING</h2>

    <ul class="service-list">
      <li><svg viewBox="0 0 32 32" aria-hidden="true"><circle cx="16" cy="16" r="13" fill="none" stroke="#fff" stroke-width="2"/><path d="M10 16.5l4 4 8-8.5" fill="none" stroke="#fff" stroke-width="2"/></svg>Road Construction</li>
      <li><svg viewBox="0 0 32 32" aria-hidden="true"><circle cx="16" cy="16" r="13" fill="none" stroke="#fff" stroke-width="2"/><path d="M10 16.5l4 4 8-8.5" fill="none" stroke="#fff" stroke-width="2"/></svg>Underground Utilities</li>
      <li><svg viewBox="0 0 32 32" aria-hidden="true"><circle cx="16" cy="16" r="13" fill="none" stroke="#fff" stroke-width="2"/><path d="M10 16.5l4 4 8-8.5" fill="none" stroke="#fff" stroke-width="2"/></svg>Site Preparation &amp; Excavation</li>
      <li><svg viewBox="0 0 32 32" aria-hidden="true"><circle cx="16" cy="16" r="13" fill="none" stroke="#fff" stroke-width="2"/><path d="M10 16.5l4 4 8-8.5" fill="none" stroke="#fff" stroke-width="2"/></svg>Shoreline Restoration</li>
    </ul>

    <div class="call-panel">
      <span>CALL US NOW</span>
      <span>555-318-2946</span>
    </div>

    <p class="contact-line">www.MarlowTerraworks.example<span class="divider">|</span>Info@MarlowTerraworks.example</p>
    <p class="licence">CUC 8841907</p>
  </main>
</body>
</html>
```